Letterhead Design Project

Initially, we would like to review our letterheads.

Something simple which uses our corporate imagery well and is nicely balanced.

Please note that I will be following up this letter-head with some customised quote templates and similarly customisable collateral in the next few weeks.

Target Market(s)

Enterprise business

Industry/Entity Type

Quote

Requirements
Must have
• The Nexora9 logo
See www.nexora9.com.au

Our tagline "Enterprise Hosting, Messaging and Server Virtualisation"

Our website address

Ideally in our colour pallette, but will consider submissions which look fantastic and necessitate other colours.

```html
<!DOCTYPE html>
<html lang="en">
<head>
<meta charset="utf-8">
<title>Nexora9 Letterhead</title>
<link rel="stylesheet" href="https://fonts.googleapis.com/css2?family=Jost:wght@500;700&display=swap">
<style>
  :root {
    --brand-red: #d0121b;
    --band-red: #c8000a;
    --ink: #2b2b2b;
    --ink-soft: #3a3a3a;
    --paper: #ffffff;
  }
  * { margin: 0; padding: 0; box-sizing: border-box; }
  html, body {
    width: 929px;
    height: 1200px;
    overflow: hidden;
    background: var(--paper);
  }
  .letterhead {
    position: relative;
    width: 929px;
    height: 1200px;
    background: var(--paper);
    font-family: "Jost", "Helvetica Neue", Arial, sans-serif;
    color: var(--ink);
  }
  .brand {
    position: absolute;
    left: 39px;
    top: 60px;
  }
  .brand-name {
    display: block;
    font-size: 38px;
    font-weight: 700;
    line-height: 1;
    letter-spacing: -0.5px;
    color: var(--ink);
  }
  .brand-url {
    margin-top: 2px;
    font-size: 14px;
    font-weight: 700;
    line-height: 1.2;
    color: var(--ink-soft);
  }
  .sender {
    position: absolute;
    left: 641px;
    top: 23px;
    display: flex;
    gap: 10px;
  }
  .sender-rule {
    width: 11px;
    height: 109px;
    background: var(--brand-red);
  }
  .sender-address {
    font-style: normal;
    font-size: 17px;
    font-weight: 700;
    line-height: 22.5px;
    color: var(--ink-soft);
    margin-top: -5px;
  }
  .footer-brand {
    position: absolute;
    right: 17px;
    top: 1100px;
  }
  .footer-brand .brand-name { font-size: 38px; }
  .tagline-band {
    position: absolute;
    left: 0;
    bottom: 0;
    width: 929px;
    height: 57px;
    background: var(--band-red);
    display: flex;
    align-items: center;
    justify-content: center;
  }
  .tagline {
    font-size: 14.5px;
    font-weight: 700;
    letter-spacing: 0.2px;
    color: var(--paper);
    padding-top: 2px;
  }
</style>
</head>
<body>
  <main class="letterhead">
    <header>
      <div class="brand">
        <span class="brand-name">Nexora9</span>
        <div class="brand-url">www.nexora9.com.au</div>
      </div>
      <div class="sender">
        <span class="sender-rule"></span>
        <address class="sender-address">
          Nexora9 Pty. Ltd.<br>
          Suite 4, Level 3<br>
          18 Calder Street,<br>
          Harwood Park, Australia<br>
          VIC - 3912
        </address>
      </div>
    </header>
    <footer>
      <div class="footer-brand">
        <span class="brand-name">Nexora9</span>
      </div>
      <div class="tagline-band">
        <p class="tagline">ENTERPRISE HOSTING | MESSAGING | SERVER VIRTUALISATION</p>
      </div>
    </footer>
  </main>
</body>
</html>
```